Visitenkarten-Design Neutrale Verzollungs Agentur für den Grenzverkehr des Zollwesens
Sehr schnelle Umsetzung nach unserer Vorstellung,und sehr netter und guter Umgang in der Kominikation. tolvix hat unsere erwartung zu 100 % übertroffen.
Zielgruppe
Wir sind eine Neutrale Verzollungs Agentur für den Grenzverkehr des Zollwesens
Bluefield & Meridian Group
Wir führen für Kunden die Zollabwicklungen ab.
Seefracht - Bahnfracht-Luftfracht-LKW Fracht
Cargo - Hersteller Firmen und Endknden International
Aufgabenstellung
Rückseite sollte mitgestaltet werden

```html
<!DOCTYPE html>
<html lang="de">
<head>
<meta charset="utf-8">
<title>Grenzlot – Visitenkarte</title>
<link rel="stylesheet" href="https://fonts.googleapis.com/css2?family=Exo+2:wght@600;700&family=Questrial&family=Open+Sans:wght@600&display=swap">
<style>
  :root {
    --stage: #c8c8c8;
    --paper: #ffffff;
    --slate: #2b3a43;
    --ink: #3e3e3e;
    --logo-grey: #4a4a4a;
    --logo-grey-dark: #555a5e;
    --accent: #3d86c6;
    --band: #f3f4f8;
    --rule: #9fb3c8;
  }
  * { margin: 0; padding: 0; box-sizing: border-box; }
  html, body { width: 1073px; height: 1200px; overflow: hidden; background: var(--stage); }
  .stage { position: relative; width: 1073px; height: 1200px; }

  .card { position: absolute; width: 790px; height: 455px; }
  .card--front { left: 140px; top: 142px; background: var(--paper); box-shadow: 0 1px 3px rgba(0,0,0,.35); }
  .card--back { left: 144px; top: 658px; width: 787px; background: var(--slate); }

  .header-band {
    position: absolute; left: 2px; right: 2px; top: 34px; height: 104px;
    background: linear-gradient(180deg, var(--band) 0%, rgba(243,244,248,.55) 70%, rgba(255,255,255,0) 100%);
  }

  .brand {
    position: absolute; display: flex; align-items: center; gap: 8px;
    font-family: "Exo 2", sans-serif; font-weight: 700; color: var(--logo-grey);
    white-space: nowrap;
  }
  .brand__dot { border-radius: 50%; background: var(--accent); flex: none; }
  .card--front .brand { left: 86px; top: 82px; height: 74px; padding: 0 18px; background: var(--paper); font-size: 32px; }
  .card--front .brand__dot { width: 14px; height: 14px; }

  .markets {
    position: absolute; left: 390px; top: 124px;
    font-family: "Open Sans", sans-serif; font-weight: 600; font-size: 14.5px; color: var(--ink);
  }

  .company {
    position: absolute; right: 468px; top: 253px; text-align: right;
    font-family: "Exo 2", sans-serif; font-weight: 600; font-size: 20px; line-height: 24.5px; color: var(--accent);
  }
  .address {
    position: absolute; right: 468px; top: 334px; text-align: right; font-style: normal;
    font-family: "Questrial", sans-serif; font-size: 20.5px; line-height: 24.5px; color: var(--ink);
  }
  .divider { position: absolute; left: 380px; top: 250px; width: 1px; height: 165px; background: var(--rule); }
  .contact {
    position: absolute; left: 448px; top: 266px;
    font-family: "Questrial", sans-serif; font-size: 20.5px; line-height: 24.5px; color: var(--ink);
  }
  .contact p + p { margin-top: 25px; }

  .card--back .brand { left: 0; right: 0; top: 198px; justify-content: center; font-size: 44px; color: var(--logo-grey-dark); gap: 12px; }
  .card--back .brand__dot { width: 20px; height: 20px; }
  .back-rule { position: absolute; left: 46px; width: 691px; top: 380px; height: 1.5px; background: #e8ecef; }
  .tagline {
    position: absolute; left: 0; right: 0; top: 399px; text-align: center;
    font-family: "Questrial", sans-serif; font-size: 17px; line-height: 19.5px; color: #ffffff;
  }
</style>
</head>
<body>
<main class="stage">
  <section class="card card--front">
    <div class="header-band" role="img" aria-label="Dezentes helles Band hinter dem Markennamen"></div>
    <div class="brand"><span class="brand__dot"></span>Grenzlot</div>
    <p class="markets">Switzerland · Germany · Denmark · France</p>

    <div class="company">Bluefield &amp; Meridian<br>Group GmbH</div>
    <address class="address">Birkenweg 118<br>A-4291 Lindenfeld</address>
    <div class="divider"></div>
    <div class="contact">
      <p>Tel: 04711/280 45-10<br>Fax: 04711/280 45-19</p>
      <p>E-mail: kontakt@grenzlot-beispiel.com<br>Web: www.grenzlot-beispiel.com</p>
    </div>
  </section>

  <section class="card card--back">
    <div class="brand"><span class="brand__dot"></span>Grenzlot</div>
    <div class="back-rule"></div>
    <p class="tagline">Bluefield &amp; Meridian Group<br>Verkauf - Vertrieb von Handelswaren &amp; Dienstleistungen</p>
  </section>
</main>
</body>
</html>
```